Volmira Logo and business card

We need a business card and logo, we are currently using a logo that we like but would like to be a bit more streamlined. We deal with very high end clients and our business card needs to reflect that. We would love to see and hire somebody that can deliver a very MODERN, simple design. With he main front of the card to be black with either a red lettering or White to provide great contrast. I would like to have a minimalist abstract picture of a heavy machine on it but it is not a requirement ( most likely an Crane ( a bold heron crane with a bucket would be perfect or maybe a vendari 270 XT )) If it keeps in line with being a classic simple, and modern design. Letterpress is also an option where it gives it a great look and texture, the card will be printed on a thick stock. On the back there needs to be a star included somewhere on the card and design, this represents the first generation that started the company back in 1936 therefore it is a sentimental addition ( make it modern and simple)
We do not want a cheesy construction template. We do heavy site work, aka we use excavators, payloaders, off road rok j40 trucks, very big fun toys.
There is a huge chance to get the web design as well for the winning design.
Have fun, cannot wait to see the designs!
In addition, we'd like to point out that our primary need and priority is still the BUSINESS CARD design itself. The logo has to complement the overall look of the business card, but it is secondary to the card's look. Please keep this in mind.
Thank you,
Gerald
Target Market(s)
General Contractors, upscale home owners ( house values of 1M plus)
and commercial property owners.
Projects range from $5000 to 1 million.
Industry/Entity Type
Construction
Requirements
Must have
- Star incorporated into design
Nice to have
- an abstract heavy site work machine ( pics attached) If it keeps in line with being a classic simple, and modern design.
I would like to have black and red on the design since all the lettering on the trucks is red, but i will let the designer take care of that.

```html
<!DOCTYPE html>
<html lang="en">
<head>
<meta charset="utf-8">
<title>Volmira business card</title>
<link href="https://fonts.googleapis.com/css2?family=Open+Sans:wght@400;700;800&display=swap" rel="stylesheet">
<style>
  :root {
    --backdrop: #161616;
    --card: #2d2d2d;
    --card-line: #242424;
    --brand-red: #c8202c;
    --text-light: #c9c9c9;
    --text-muted: #9a9a9a;
    --star-silver: #d8d8d8;
  }
  * { margin: 0; padding: 0; box-sizing: border-box; }
  html, body {
    width: 1200px; height: 1000px; overflow: hidden;
    background: var(--backdrop);
    font-family: "Open Sans", sans-serif;
  }
  .canvas {
    position: relative; width: 1200px; height: 1000px;
    display: flex; align-items: center; justify-content: center; gap: 60px;
  }
  .card {
    position: relative; width: 510px; height: 292px;
    background: var(--card);
    box-shadow: 0 14px 30px rgba(0,0,0,.55);
    overflow: hidden;
  }
  .card-stripes { position: absolute; left: 0; top: 0; width: 100%; height: 100%; }
  .card-star { position: absolute; }

  /* contact side */
  .contact-name {
    position: absolute; left: 34px; top: 30px;
    color: var(--brand-red); font-weight: 700; font-size: 17px;
  }
  .contact-role { position: absolute; left: 34px; top: 53px; color: var(--text-light); font-size: 11px; }
  .contact-lines { position: absolute; left: 34px; top: 82px; color: var(--text-light); font-size: 11px; line-height: 16px; }
  .contact-address { position: absolute; left: 34px; bottom: 34px; color: var(--text-light); font-size: 11px; line-height: 16px; }
  .contact-side .card-star { left: 300px; top: 160px; width: 120px; height: 116px; }
  .contact-side .brand-name { position: absolute; left: 288px; top: 96px; color: var(--brand-red); }

  /* brand side */
  .brand-side .card-star { left: 52px; top: 92px; width: 122px; height: 118px; }
  .brand-name {
    font-weight: 800; font-size: 44px; letter-spacing: 1px; text-transform: uppercase;
  }
  .brand-side .brand-name { position: absolute; left: 280px; top: 72px; color: #ffffff; }
  .brand-locale {
    position: absolute; left: 296px; top: 134px;
    color: var(--brand-red); font-weight: 700; font-size: 12px; letter-spacing: 2px; text-transform: uppercase;
  }
  .brand-web {
    position: absolute; left: 304px; top: 204px;
    color: var(--text-muted); font-size: 12px; letter-spacing: 2px;
  }
</style>
</head>
<body>
<main class="canvas">

  <section class="card contact-side">
    <svg class="card-stripes" viewBox="0 0 510 292" aria-hidden="true">
      <g stroke="var(--card-line)" stroke-width="1.5">
        <line x1="0" y1="138" x2="510" y2="138"/><line x1="0" y1="148" x2="510" y2="148"/>
        <line x1="0" y1="158" x2="510" y2="158"/><line x1="0" y1="168" x2="510" y2="168"/>
        <line x1="0" y1="178" x2="510" y2="178"/><line x1="0" y1="188" x2="510" y2="188"/>
        <line x1="0" y1="198" x2="510" y2="198"/><line x1="0" y1="208" x2="510" y2="208"/>
        <line x1="0" y1="218" x2="510" y2="218"/><line x1="0" y1="228" x2="510" y2="228"/>
        <line x1="0" y1="238" x2="510" y2="238"/>
      </g>
    </svg>
    <p class="contact-name">Dana Ferris</p>
    <p class="contact-role">Accountant</p>
    <p class="contact-lines">+61 400 555 218<br>dana@volmira.com</p>
    <p class="contact-address">48 Quarry Lane<br>Riverton North NSW 20480</p>
    <p class="brand-name">Volmira</p>
    <svg class="card-star" viewBox="0 0 100 95" aria-hidden="true">
      <polygon fill="var(--star-silver)" points="50,0 61.8,36.3 100,36.3 69.1,58.8 80.9,95 50,72.6 19.1,95 30.9,58.8 0,36.3 38.2,36.3"/>
    </svg>
  </section>

  <section class="card brand-side">
    <svg class="card-stripes" viewBox="0 0 510 292" aria-hidden="true">
      <g stroke="var(--card-line)" stroke-width="1.5">
        <line x1="0" y1="82" x2="510" y2="82"/><line x1="0" y1="92" x2="510" y2="92"/>
        <line x1="0" y1="102" x2="510" y2="102"/><line x1="0" y1="112" x2="510" y2="112"/>
        <line x1="0" y1="122" x2="510" y2="122"/><line x1="0" y1="132" x2="510" y2="132"/>
        <line x1="0" y1="142" x2="510" y2="142"/><line x1="0" y1="152" x2="510" y2="152"/>
        <line x1="0" y1="162" x2="510" y2="162"/><line x1="0" y1="172" x2="510" y2="172"/>
        <line x1="0" y1="182" x2="510" y2="182"/><line x1="0" y1="192" x2="510" y2="192"/>
        <line x1="0" y1="202" x2="510" y2="202"/>
      </g>
    </svg>
    <svg class="card-star" viewBox="0 0 100 95" aria-hidden="true">
      <polygon fill="var(--star-silver)" points="50,0 61.8,36.3 100,36.3 69.1,58.8 80.9,95 50,72.6 19.1,95 30.9,58.8 0,36.3 38.2,36.3"/>
    </svg>
    <p class="brand-name">Volmira</p>
    <p class="brand-locale">Ashford Ridge</p>
    <p class="brand-web">www.volmira.com</p>
  </section>

</main>
</body>
</html>
```